Responsive WordPress website for medical therapy practice consulting business.

We need both design and website for responsive Wordpress website. The use of Tessaly theme is preferred when considering the design (not required).
Site must be designed for 1920px width and fully responsive.
See full scope of the project below.

DESIGN:
Design a full screen layout using images and parallax movement where appropriate.
Easy to use navigation for desktop and hamburger style navigation for mobile devices.
Create an original design for the home, sub-page template.
Create a responsive website using common desktop breakpoints 1920, 1366, 1280 1024 as well as mobile devices.
Color scheme should use soft or pastel color avoiding reds.
Design will take inspiration from logo design and color scheme.
Large “Hero slider” may be employed to striking visual interest.
The website will focus the content on the Homepage mission statement, What We Do and How to Reach Us, content.
Website Footer Information: Include content for Privacy Policy and Terms of Use, address and copyright information.

DEVELOPMENT NOTES:

WordPress content management platform will be used .

Responsive grid will be used to properly display website content on all devices including mobile, laptop and desktop at standard breakpoints.

Social Media links to LinkedIn and Twitter

Google Analytics and Search Console integration – allows tracking of visitors and in-depth search data, indexing and performance.

Yoast Basic SEO – basic setup and integration is included in the proposal. This includes creating SEO friendly page titles, search descriptions and best practices for heading and image tags.

508 & ADA compliance

PAGE LIST:
The following pages are a list of current websites pages. These are used as a guideline for developing the proposal and can be changed to reflect content:

NAVIGATION LINKS:

HOME

· Featuring the new logo, the home page will display Brenlow Care Advisor’s message, services, and contact information.
· The navigation will be prominent, intuitive and easy to use, allowing to find information quickly.
· Parallax scrolling will provide a cool modern visual effect without being overbearing.

====================================================

ABOUT US –

· History
· Bios
· Links

SERVICES

· Business Consultancy service

CONTACT US – This section will present ways for viewers to reach out either by phone, email.

· Google map of office locations.
· Business information
a. Locations
b. Address
c. Phone
d. Fax
e. Email

FOOTER LINKS – Additional information for legal or usage claims, company info and contact info.

· Copyright information
· Links to CONTACT
· Social Media
· Disclaimer
· Privacy policy
· Terms of use

```html
<!DOCTYPE html>
<html lang="en">
<head>
<meta charset="utf-8">
<title>Brenlow Care Advisor’s</title>
<link rel="stylesheet" href="https://fonts.googleapis.com/css2?family=Questrial&display=swap">
<style>
:root{
  --blue:#0b5fb8;
  --blue-deep:#0a4fa8;
  --blue-light:#1a8ad6;
  --ink:#1b1b1b;
  --text:#2a2a2a;
  --band:#eef5fd;
  --field:#8a8a8a;
  --field-text:#a0a0a0;
  --footer:#2b2b2b;
  --white:#ffffff;
}
*{box-sizing:border-box;margin:0;padding:0}
html,body{width:1200px;height:2293px;overflow:hidden}
body{position:relative;font-family:"Questrial",sans-serif;color:var(--text);background:var(--white)}

/* shared */
.brand{position:absolute;left:0;width:1200px;display:flex;align-items:center;justify-content:center;gap:10px;letter-spacing:.3px}
.brand-mark{width:12px;height:12px;background:currentColor}
.section-title{position:absolute;font-size:24px;font-weight:400;color:var(--ink);text-transform:uppercase;letter-spacing:.5px}
.section-title::after{content:"";position:absolute;left:0;bottom:-9px;width:46px;height:2px;background:var(--blue)}

/* hero */
.hero-photo{position:absolute;left:0;top:0;width:1200px;height:674px;
  background:linear-gradient(180deg,#1460b4 0%,#1670c2 55%,#1b8ad3 100%)}
.hero-brand{top:38px;color:var(--white);font-size:18px}
.nav{position:absolute;top:99px;left:456px;display:flex;gap:27px;font-size:11.5px;color:var(--white);text-transform:uppercase}
.nav .active{border-bottom:2px solid var(--white);padding-bottom:4px}
.dropdown{position:absolute;left:518px;top:125px;width:80px;background:var(--white);font-size:10px;text-transform:uppercase;color:var(--ink);box-shadow:0 2px 6px rgba(0,0,0,.2);list-style:none}
.dropdown li{height:20px;line-height:20px;padding:0 12px}
.dropdown li.current{background:var(--blue-light);color:var(--white)}
.hero-title{position:absolute;top:315px;left:0;width:1200px;text-align:center;color:var(--white);font-size:25px;font-weight:400;line-height:36px;text-transform:uppercase;letter-spacing:.3px}
.hero-text{position:absolute;top:400px;left:355px;width:490px;text-align:center;color:var(--white);font-size:12px;line-height:16px}
.btn-contact{position:absolute;left:509px;top:476px;width:181px;height:39px;background:var(--white);color:var(--blue-deep);font-size:16px;display:flex;align-items:center;justify-content:center}

/* intro */
.intro-brand{top:785px;color:var(--blue-deep);font-size:22px}
.intro-text{position:absolute;top:866px;left:288px;width:624px;text-align:center;font-size:11.6px;line-height:15.4px}

/* services */
.services-band{position:absolute;left:0;top:1076px;width:1200px;height:445px;background:var(--band)}
.photo{position:absolute}
.photo-team{left:174px;top:1150px;width:234px;height:234px;background:linear-gradient(160deg,#c9d6e2,#6f7a86);box-shadow:6px 6px 14px rgba(0,0,0,.25)}
.photo-meeting{left:408px;top:1232px;width:150px;height:234px;background:linear-gradient(170deg,#dfe6ec,#a89c90)}
.photo-desk{left:269px;top:1384px;width:139px;height:82px;background:linear-gradient(180deg,#e2e4e6,#b9b3ad)}
.services-title{left:618px;top:1179px}
.service-name{position:absolute;left:618px;top:1266px;font-size:15px;color:var(--ink);font-weight:700}
.service-text{position:absolute;left:618px;top:1304px;width:384px;font-size:12.2px;line-height:15.6px;color:var(--text)}
.service-text b{color:var(--ink)}

/* contact */
.contact-title{left:202px;top:1619px}
.field{position:absolute;left:202px;width:270px;height:31px;border:1px solid var(--field);background:var(--white);font-size:12px;color:var(--field-text);padding:7px 11px}
.field-message{height:107px}
.btn-submit{position:absolute;left:202px;top:1957px;width:124px;height:26px;background:linear-gradient(90deg,var(--blue-light),var(--blue-deep));color:var(--white);font-size:12px;font-weight:700;display:flex;align-items:center;justify-content:center}
.map{position:absolute;left:576px;top:1610px;width:450px;height:390px;background:linear-gradient(135deg,#e7eae7,#dfe4df)}

/* footer */
.footer{position:absolute;left:0;top:2087px;width:1200px;height:206px;background:var(--footer);color:var(--white);font-size:11px}
.footer-line{position:absolute;left:0;width:1200px;display:flex;justify-content:center;align-items:center;gap:7px;height:14px}
.footer-line svg{fill:var(--blue-light)}
.social{position:absolute;top:140px;left:543px;display:flex;gap:4px}
.social span{width:20px;height:20px;background:var(--blue-light);display:block}
.legal{position:absolute;top:176px;left:0;width:1200px;text-align:center;font-size:10.5px;color:var(--white)}
</style>
</head>
<body>

<header class="hero">
  <div class="hero-photo" role="img" aria-label="Hero photo of colleagues talking in a bright office, tinted blue"></div>
  <div class="brand hero-brand"><span class="brand-mark"></span>Brenlow Care Advisor’s</div>
  <nav class="nav">
    <span class="active">Home</span><span>About Us</span><span>Services</span><span>Contact Us</span>
  </nav>
  <ul class="dropdown">
    <li class="current">History</li><li>Bios</li><li>Links</li>
  </ul>
  <h1 class="hero-title">Lorem ipsum dolor sit amet,<br>consectetur adipiscing elit, sed</h1>
  <p class="hero-text">Lorem ipsum dolor sit amet, consectetur adipiscing elit, sed do eiusmod tempor incididunt ut labore et dolore magna aliqua. Quis ipsum suspendisse ultrices gravida. Risus commodo viverra maecenas accumsan lacus vel facilisis.</p>
  <a class="btn-contact">Contact Now</a>
</header>

<section class="intro">
  <div class="brand intro-brand"><span class="brand-mark"></span>Brenlow Care Advisor’s</div>
  <p class="intro-text">Lorem ipsum dolor sit amet, consectetur adipiscing elit, sed do eiusmod tempor incididunt ut labore et dolore magna aliqua. Quis ipsum suspendisse ultrices gravida. Risus commodo viverra maecenas accumsan lacus vel facilisis. Lorem ipsum dolor sit amet, consectetur adipiscing elit, sed do eiusmod tempor incididunt ut labore et dolore magna aliqua. Quis ipsum suspendisse ultrices gravida. Risus commodo viverra maecenas accumsan lacus vel facilisis. Lorem ipsum dolor sit amet, consectetur adipiscing elit, sed do eiusmod tempor incididunt ut labore et dolore magna aliqua. Quis ipsum suspendisse ultrices gravida. Risus commodo viverra maecenas accumsan lacus vel facilisis.</p>
</section>

<section class="services">
  <div class="services-band"></div>
  <div class="photo photo-meeting" role="img" aria-label="Photo of a team working around a tablet at a meeting table"></div>
  <div class="photo photo-desk" role="img" aria-label="Photo of hands on a desk during a meeting"></div>
  <div class="photo photo-team" role="img" aria-label="Photo of three business people in suits reviewing a tablet"></div>
  <h2 class="section-title services-title">Our Services</h2>
  <h3 class="service-name">Business Consultancy Service</h3>
  <p class="service-text">Lorem ipsum dolor sit amet, consectetur adipiscing elit, sed do eiusmod tempor incididunt ut labore et dolore magna aliqua. Quis ipsum suspendisse ultrices gravida. Risus commodo viverra maecenas accumsan lacus vel facilisis. Lorem ipsum dolor sit amet, consectetur adipiscing elit, sed do eiusmod tempor incididunt ut labore et dolore magna aliqua. Quis ipsum suspendisse ultrices gravida. Risus commodo viverra maecenas accumsan lacus vel facilisis. <b>Read More &gt;&gt;</b></p>
</section>

<section class="contact">
  <h2 class="section-title contact-title">Contact Us</h2>
  <div class="field" style="top:1701px">Name</div>
  <div class="field" style="top:1744px">Email</div>
  <div class="field" style="top:1787px">Phone Number</div>
  <div class="field field-message" style="top:1831px">Message</div>
  <a class="btn-submit">Submit</a>
  <div class="map" role="img" aria-label="Map of the office location and surrounding streets"></div>
</section>

<footer class="footer">
  <div class="footer-line" style="top:28px"><svg width="12" height="11" viewBox="0 0 12 11"><path d="M6 0 12 5.5H10V11H7.5V7.5h-3V11H2V5.5H0z"/></svg>Lorem ipsum dolor sit amet, consectetur adipiscing elit, sed do</div>
  <div class="footer-line" style="top:46px"><svg width="10" height="10" viewBox="0 0 10 10"><circle cx="5" cy="5" r="5"/></svg>www.brenlowcare.com</div>
  <div class="footer-line" style="top:62px"><svg width="10" height="10" viewBox="0 0 10 10"><path d="M2 0 4 2.5 3 4Q4 6.5 6 7L7.5 6 10 8 8.5 10Q1 9 0 1.5z"/></svg>555 010 2244</div>
  <div class="footer-line" style="top:78px"><svg width="11" height="8" viewBox="0 0 11 8"><path d="M0 0h11v8H0z"/><path d="M0 0 5.5 4.5 11 0" stroke="#2b2b2b" fill="none"/></svg>support@brenlowcare.com</div>
  <div class="footer-line" style="top:94px"><svg width="11" height="10" viewBox="0 0 11 10"><path d="M2.5 0h6v3h-6zM0 3.5h11V8H9v2H2V8H0z"/></svg>555 010 2245</div>
  <div class="social" aria-label="Social media links">
    <span></span><span></span><span></span><span></span><span></span>
  </div>
  <p class="legal">© 2019 Brenlow. All Rights Reserved &nbsp;|&nbsp; Privacy Policy &nbsp;|&nbsp; Terms of use</p>
</footer>

</body>
</html>
```